Business Cards for a Junk Removal Company

Hello,
We are looking to have business cards designed that are simple, bold, easy to read, and right to the point. Please see the attachments for our logo files. We want the card to be yellow on both sides ( Color code Yellow: #FFE01B). The logo text font is (Rockstar Extra Bold) and this is also in the files attached. Please make the text black for the logo. On the back side of the card, you can use white and black for text. Thank you in advance for your hard work!

Front of card-
Harbor Haul Away (logo)
Back of card-
Harbor Haul Away
Donate - Recycle - Dispose
555-271-8093
www.harborhaulaway.example
info@harborhaulaway.example

Industry/Entity Type

Junk removal

Contact Information for Business Card

FRONT OF CARD- Harbor Haul Away (logo) BACK OF CARD- Harbor Haul Away Donate - Recycle - Dispose 555-271-8093 www.harborhaulaway.example info@harborhaulaway.example

Font styles to use
Other font styles liked:
• Rockstar Extra Bold

Colors
FFF300
FFF600
FEFA6F
FFFEC7
FFFEE8

Requirements
Must have
• Must have color code Yellow: #FFE01B for the background of front and back of the card

```html
<!DOCTYPE html>
<html lang="en">
<head>
<meta charset="utf-8">
<title>Harbor Haul Away — Business Cards</title>
<link href="https://fonts.googleapis.com/css2?family=Inter:wght@400;800&display=swap" rel="stylesheet">
<style>
  :root {
    --page-bg: #d6d6d6;
    --card-yellow: #FFE01B;
    --ink: #111111;
    --card-shadow: rgba(0, 0, 0, 0.18);
  }
  * { box-sizing: border-box; margin: 0; padding: 0; }
  html, body {
    width: 1200px;
    height: 1051px;
    overflow: hidden;
    background: var(--page-bg);
    font-family: "Inter", Arial, sans-serif;
    color: var(--ink);
  }
  .sheet {
    position: relative;
    width: 1200px;
    height: 1051px;
    display: flex;
    align-items: center;
    justify-content: center;
    gap: 40px;
  }
  .card {
    width: 540px;
    height: 309px;
    background: var(--card-yellow);
    box-shadow: 0 18px 40px var(--card-shadow);
    display: flex;
    flex-direction: column;
    align-items: center;
    justify-content: center;
    text-align: center;
  }
  .brand-name {
    font-weight: 800;
    color: var(--ink);
    text-transform: uppercase;
    letter-spacing: 0.02em;
    line-height: 1;
  }
  .card--front .brand-name { font-size: 46px; }
  .card--back .brand-name { font-size: 34px; }
  .tagline {
    margin-top: 12px;
    font-size: 15px;
    font-weight: 400;
  }
  .divider {
    width: 64px;
    height: 1.5px;
    background: var(--ink);
    margin: 14px 0 16px;
  }
  .contact-list {
    list-style: none;
    font-size: 15px;
    font-weight: 400;
    line-height: 1.45;
  }
</style>
</head>
<body>
  <main class="sheet">
    <section class="card card--back" aria-label="Back of card">
      <h2 class="brand-name">Harbor Haul Away</h2>
      <p class="tagline">Donate - Recycle - Dispose</p>
      <div class="divider"></div>
      <ul class="contact-list">
        <li class="contact-phone">555-271-8093</li>
        <li class="contact-web">www.harborhaulaway.example</li>
        <li class="contact-email">info@harborhaulaway.example</li>
      </ul>
    </section>
    <section class="card card--front" aria-label="Front of card">
      <h1 class="brand-name">Harbor Haul Away</h1>
    </section>
  </main>
</body>
</html>
```